70th Whitcombe Gallery Gala Event postcard

We are looking at a design that uses the word "Evolutionary" - - then the tagline Color, Culture, Creativity. 70th Anniversary Platinum EventI was thinking of the old car ads that talk about the new car coming out next year as Evolutionary in design.. We are having and event to raise money for a new art gallery - in a way this is a new and improved gallery. This is also our "platinum" year. My first thought it that this would be Platinum/ chrome ink on black background. .. It does not have to be a car, but maybe have the look of a car fin. Possibly incorporate red or purple. We have a logo that is different shades of orange, but I can see this being different shades of another color - or chrome. The car fin photos are not mine.. they are mainly for style ideas.. Not to be used in the final design. - i made up a quick idea of my own.. but not good at creating the chrome looking effect. Also not really enough line on mine.

Requirements
Must have
• Logo - but preferably not orange.. would like shades of chrome if possible
• Words in metallic. 4X6 postcard.
Should not have
• Actual car photos - those were borrowed

```html
<!DOCTYPE html>
<html lang="en">
<head>
<meta charset="utf-8">
<title>Whitcombe Gallery Guild – Evolutionary</title>
<link rel="stylesheet" href="https://fonts.googleapis.com/css2?family=Josefin+Sans:wght@600;700&family=Open+Sans:wght@500&display=swap">
<style>
  :root {
    --ink: #050507;
    --ember: #8a2a10;
    --ember-deep: #3a0f06;
    --steel-dark: #1b1e24;
    --chrome-hi: #ffffff;
    --chrome-mid: #c9ccd2;
    --chrome-low: #7d8189;
    --rule-red: #d0101e;
    --logo-orange: #f26a21;
    --logo-gold: #f7b21b;
  }
  * { margin: 0; padding: 0; box-sizing: border-box; }
  html, body { width: 800px; height: 1200px; overflow: hidden; background: var(--ink); }
  .postcard {
    position: relative;
    width: 800px;
    height: 1200px;
    overflow: hidden;
    background: var(--ink);
  }
  .backdrop {
    position: absolute;
    inset: 0;
    background:
      radial-gradient(ellipse 60% 25% at 10% 0%, var(--ember) 0%, transparent 70%),
      radial-gradient(ellipse 70% 22% at 95% 8%, var(--ember-deep) 0%, transparent 70%),
      radial-gradient(ellipse 90% 20% at 40% 100%, var(--ember) 0%, transparent 75%),
      linear-gradient(160deg, var(--ink) 0%, var(--steel-dark) 45%, var(--ink) 75%);
  }
  .brand-mark {
    position: absolute;
    left: 233px;
    top: 80px;
    width: 334px;
    height: 334px;
  }
  .chrome {
    background: linear-gradient(180deg, var(--chrome-hi) 0%, var(--chrome-mid) 45%, var(--chrome-low) 55%, var(--chrome-hi) 100%);
    -webkit-background-clip: text;
    background-clip: text;
    color: transparent;
  }
  .title-block {
    position: absolute;
    left: 0;
    width: 800px;
    text-align: center;
    font-family: "Josefin Sans", sans-serif;
    font-weight: 700;
    line-height: 1;
  }
  .gallery-name { top: 518px; font-size: 112px; letter-spacing: 6px; }
  .gallery-guild { top: 680px; font-size: 60px; letter-spacing: 10px; }
  .rule {
    position: absolute;
    left: 93px;
    width: 654px;
    height: 3px;
    background: var(--rule-red);
  }
  .rule-top { top: 758px; }
  .rule-bottom { top: 920px; }
  .theme { top: 790px; font-size: 70px; letter-spacing: 5px; }
  .tagline { top: 872px; font-size: 33px; letter-spacing: 3px; }
  .occasion {
    position: absolute;
    left: 0;
    top: 960px;
    width: 800px;
    text-align: center;
    font-family: "Open Sans", sans-serif;
    font-weight: 500;
    font-size: 48px;
    line-height: 68px;
  }
</style>
</head>
<body>
<main class="postcard">
  <div class="backdrop" role="img" aria-label="Dark glossy car fin in black chrome with warm red reflections"></div>

  <svg class="brand-mark" viewBox="0 0 334 334" aria-hidden="true">
    <defs>
      <linearGradient id="markFill" x1="0" y1="0" x2="1" y2="1">
        <stop offset="0" stop-color="var(--logo-orange)"/>
        <stop offset="1" stop-color="var(--logo-gold)"/>
      </linearGradient>
    </defs>
    <circle cx="167" cy="167" r="160" fill="url(#markFill)"/>
  </svg>

  <h1 class="title-block gallery-name chrome">WHITCOMBE</h1>
  <p class="title-block gallery-guild chrome">GALLERY GUILD</p>
  <div class="rule rule-top"></div>
  <h2 class="title-block theme chrome">EVOLUTIONARY</h2>
  <p class="title-block tagline chrome">COLOR, CULTURE, CREATIVITY</p>
  <div class="rule rule-bottom"></div>
  <p class="occasion chrome">70th Anniversary<br>Platinum Event</p>
</main>
</body>
</html>
```